Project 3) Gather the Lanterns Screenplay Book

Beth,

I do not need the Audiobook image, so can you adjust this price once we finalize this 3rd Project?

Thanks!

Leopold Varnick

```html
<!DOCTYPE html>
<html lang="en">
<head>
<meta charset="utf-8">
<title>Gather the Lanterns Screenplay Book</title>
<link href="https://fonts.googleapis.com/css2?family=Bebas+Neue&family=Montserrat:wght@500&display=swap" rel="stylesheet">
<style>
  :root {
    --frame: #000000;
    --paper: #f2efe8;
    --signal-red: #e02a15;
    --ink: #0a0a0a;
    --white: #ffffff;
  }
  html, body {
    margin: 0;
    padding: 0;
    width: 1200px;
    height: 1200px;
    overflow: hidden;
    background: var(--frame);
  }
  .cover {
    display: block;
    width: 1200px;
    height: 1200px;
  }
  .cover__paper { fill: var(--paper); }
  .cover__band { fill: var(--signal-red); }
  .cover__bubble { fill: var(--paper); }
  .project-label {
    font-family: "Montserrat", sans-serif;
    font-weight: 500;
    font-size: 44px;
    letter-spacing: 8px;
    fill: var(--ink);
  }
  .title {
    font-family: "Bebas Neue", sans-serif;
    fill: var(--signal-red);
  }
  .title--top { font-size: 206px; }
  .title--main { font-size: 274px; }
  .title--sub { font-size: 122px; }
  .author {
    font-family: "Montserrat", sans-serif;
    font-weight: 500;
    font-size: 52px;
    letter-spacing: 9px;
    fill: var(--white);
  }
</style>
</head>
<body>
<svg class="cover" viewBox="0 0 1200 1200" xmlns="http://www.w3.org/2000/svg">
  <rect class="cover__paper" x="72" y="72" width="1056" height="1056"/>
  <rect class="cover__band" x="72" y="533" width="1056" height="595"/>
  <g class="cover__bubble">
    <path d="M183 533 A417 417 0 0 0 1017 533 Z"/>
    <path d="M640 942 C690 990 750 1003 798 993 C760 982 738 960 728 930 Z"/>
  </g>

  <text class="project-label" x="1047" y="179" text-anchor="end">PROJECT 3</text>

  <text class="title title--top" x="279" y="460" textLength="652" lengthAdjust="spacingAndGlyphs">GATHER THE</text>
  <text class="title title--main" x="279" y="671" textLength="639" lengthAdjust="spacingAndGlyphs">LANTERNS</text>
  <text class="title title--sub" x="279" y="775" textLength="636" lengthAdjust="spacingAndGlyphs">SCREENPLAY BOOK</text>

  <text class="author" x="600" y="1085" text-anchor="middle">LEOPOLD VARNICK</text>
</svg>
</body>
</html>
```